Business card design needed

I have started a new business called Marlow Auto Electrical, although the words Marlow Auto Electrical will be used on signage and documents I actually want to market the business as MAE. The services I offer are Mobile Auto Electrical, Automotive Air Conditioning and Test And Tag. My business will be targetting the Mining Industry, Civil, Rail, Agricultural and Workshop Testing And Tagging. My auto electrical service ranges from fault finding to new vehicle and mine compliance fit outs. I have a very strong focus on quality workmanship. I will upload the logo I have designed and want to use I am happy for the logo colour to change but the design itself must stay the same. I want the design to have a modern, eye catching, energetic feel. As I am a passionate motorsport fan I am happy for this to also influence the design. I am happy for the front of the card to have only the emblem and logo design and the back to have all the info.

Industry/Entity Type

Electrical

Contact Information for Business Card

MAE Marlow Auto Electrical, Glen Tavish, Auto Electrician, Mobile No 0417268354

Requirements
Must have
• On the business card it is mandatory that the following license numbers are shown:

MVRL83742
PXB L731406
ABN 48 913 260 154

```html
<!DOCTYPE html>
<html lang="en">
<head>
<meta charset="utf-8">
<title>Marlow Auto Electrical – Business Card Options</title>
<link rel="stylesheet" href="https://fonts.googleapis.com/css2?family=Ubuntu:wght@400;500;700&display=swap">
<style>
  :root {
    --backdrop: #4a3f35;
    --card-orange: #e5761b;
    --card-dark: #2a2320;
    --ink-dark: #2b2624;
    --accent-orange: #ee7d22;
    --accent-soft: #d9742a;
    --paper-white: #ffffff;
    --label-white: #f4f1ec;
  }
  * { margin: 0; padding: 0; box-sizing: border-box; }
  html, body {
    width: 1200px;
    height: 634px;
    overflow: hidden;
    background: var(--backdrop);
    font-family: "Ubuntu", sans-serif;
  }
  .presentation {
    position: relative;
    width: 1200px;
    height: 634px;
  }
  .option-number {
    position: absolute;
    top: 80px;
    font-size: 44px;
    font-weight: 700;
    color: var(--label-white);
  }
  .option-number--one { left: 302px; }
  .option-number--two { left: 860px; }

  .card {
    position: absolute;
    top: 132px;
    width: 533px;
    height: 336px;
    background: var(--card-orange);
    overflow: hidden;
    box-shadow: 0 4px 14px rgba(0,0,0,0.35);
  }
  .card--one { left: 45px; }
  .card--two { left: 635px; }

  .brand {
    position: absolute;
    left: 0;
    width: 100%;
    text-align: center;
    color: var(--ink-dark);
  }
  .card--one .brand { top: 20px; left: -48px; }
  .card--two .brand { top: 28px; left: -20px; }
  .brand-mark {
    font-size: 104px;
    font-weight: 700;
    line-height: 1;
    letter-spacing: 2px;
  }
  .brand-name {
    margin-top: 4px;
    font-size: 19px;
    font-weight: 700;
    letter-spacing: -0.3px;
  }

  .info-band {
    position: absolute;
    left: 0;
    width: 100%;
    background: var(--card-dark);
  }
  .card--one .info-band { top: 207px; height: 129px; }
  .card--two .info-band { top: 207px; height: 92px; }

  .holder-name {
    position: absolute;
    font-size: 24px;
    font-weight: 700;
    color: var(--accent-orange);
  }
  .holder-role {
    position: absolute;
    font-size: 16px;
    color: var(--accent-soft);
  }
  .holder-phone {
    position: absolute;
    font-size: 19px;
    color: var(--accent-orange);
  }
  .card--one .holder-name { left: 30px; top: 13px; }
  .card--one .holder-role { left: 30px; top: 44px; }
  .card--one .holder-phone { left: 30px; top: 78px; }
  .card--two .holder-name { left: 68px; top: 11px; }
  .card--two .holder-role { left: 68px; top: 42px; }
  .card--two .holder-phone { left: 346px; top: 40px; }

  .licences {
    position: absolute;
    left: 321px;
    top: 16px;
    list-style: none;
    font-size: 18px;
    line-height: 30px;
    color: var(--accent-orange);
  }

  .licence-strip {
    position: absolute;
    left: 0;
    top: 299px;
    width: 100%;
    height: 37px;
    display: flex;
    align-items: center;
    justify-content: center;
    gap: 14px;
    font-size: 17px;
    color: var(--paper-white);
  }
</style>
</head>
<body>
<main class="presentation">
  <span class="option-number option-number--one">1</span>
  <span class="option-number option-number--two">2</span>

  <section class="card card--one" aria-label="Business card option 1">
    <div class="brand">
      <div class="brand-mark">MAE</div>
      <div class="brand-name">MARLOW AUTO ELECTRICAL</div>
    </div>
    <div class="info-band">
      <p class="holder-name">Glen Tavish</p>
      <p class="holder-role">Auto Electrician</p>
      <p class="holder-phone">0417268354</p>
      <ul class="licences">
        <li>MVRL83742</li>
        <li>PXB L731406</li>
        <li>ABN 48 913 260 154</li>
      </ul>
    </div>
  </section>

  <section class="card card--two" aria-label="Business card option 2">
    <div class="brand">
      <div class="brand-mark">MAE</div>
      <div class="brand-name">MARLOW AUTO ELECTRICAL</div>
    </div>
    <div class="info-band">
      <p class="holder-name">Glen Tavish</p>
      <p class="holder-role">Auto Electrician</p>
      <p class="holder-phone">0417268354</p>
    </div>
    <p class="licence-strip">
      <span>MVRL83742</span>
      <span>PXB L731406</span>
      <span>ABN 48 913 260 154</span>
    </p>
  </section>
</main>
</body>
</html>
```